Organic rose water based skincare line in need of product label and packaging design

We are looking for a simple, clean, modern labeling and packaging design for 2 of our products. Our brand's demographic is upscale females ages 20-40. We want our packaging to be very minimalistic, and instagramable.

Product #1: Rose water facial spray "Lumi Mist"
Product #2: Rose water facial toner "Velvet Hush Hour"

Please see attached images for our current logo and label design. We have also added some images that inspire our branding.

Target Market(s)

trendy woman ages 20-40

Industry/Entity Type

Skin Care Product

Font styles to use
Serif
Sans Serif

Colors

Designer to choose only greyscale colors for use in the design.

Requirements
Must have
• Must have our logo, bottle size, product name on front and how to use and ingredient on the back. Please see project description and attached images for more information.
Should not have
• Too much going on or too many colors.

```html
<!DOCTYPE html>
<html lang="en">
<head>
<meta charset="utf-8">
<title>Lumi Mist – Label</title>
<link href="https://fonts.googleapis.com/css2?family=Playfair+Display:wght@500&family=Roboto+Condensed:wght@400&family=Arimo:wght@400&display=swap" rel="stylesheet">
<style>
  :root {
    --backdrop: #aed5d6;
    --label: #e6f6f5;
    --label-shade: #d7ecec;
    --ink: #161616;
    --ink-soft: #2a2a2a;
    --art: #dfe9e8;
    --art-edge: #cfdcdc;
  }
  * { box-sizing: border-box; margin: 0; padding: 0; }
  html, body {
    width: 1200px;
    height: 960px;
    overflow: hidden;
    background: var(--backdrop);
  }
  .canvas {
    position: relative;
    width: 1200px;
    height: 960px;
    display: flex;
    align-items: center;
    justify-content: center;
  }
  .label {
    position: relative;
    width: 440px;
    height: 760px;
    background: linear-gradient(100deg, var(--label-shade) 0%, var(--label) 45%, var(--label) 100%);
    border-radius: 18px;
  }
  .brand {
    position: absolute;
    left: 44px;
    top: 62px;
    display: flex;
    align-items: center;
    gap: 10px;
  }
  .brand-dot {
    width: 10px;
    height: 10px;
    border-radius: 50%;
    background: var(--ink);
  }
  .brand-name {
    font-family: "Arimo", sans-serif;
    font-weight: 400;
    font-size: 24px;
    line-height: 1;
    letter-spacing: 1px;
    color: var(--ink);
  }
  .floral-art {
    position: absolute;
    left: 170px;
    top: 120px;
    width: 240px;
    height: 280px;
    border-radius: 48% 52% 40% 44%;
    background: radial-gradient(circle at 60% 45%, var(--art) 0%, var(--art) 55%, var(--label) 100%);
    border: 1px solid var(--art-edge);
  }
  .product-name {
    position: absolute;
    left: 44px;
    top: 420px;
    font-family: "Playfair Display", serif;
    font-weight: 500;
    font-size: 88px;
    line-height: 0.95;
    letter-spacing: -1px;
    color: var(--ink);
  }
  .product-desc {
    position: absolute;
    left: 48px;
    top: 620px;
    font-family: "Arimo", sans-serif;
    font-size: 22px;
    line-height: 1.45;
    color: var(--ink-soft);
  }
  .volume {
    position: absolute;
    left: 48px;
    bottom: 40px;
    font-family: "Arimo", sans-serif;
    font-size: 14px;
    color: var(--ink-soft);
  }
</style>
</head>
<body>
  <main class="canvas">
    <section class="label">
      <div class="floral-art" role="img" aria-label="Fine line drawing of an open rose with flowing stem lines"></div>
      <div class="brand">
        <span class="brand-dot"></span>
        <span class="brand-name">Petalune</span>
      </div>
      <h1 class="product-name">LUMI<br>MIST</h1>
      <p class="product-desc">Organic rosewater<br>Hydrating mist</p>
      <p class="volume">2 oz / 60 ml</p>
    </section>
  </main>
</body>
</html>
```